Real eatate

My company name is “Maple Crest Realestate” i would like to create a business card. I would like something modern and sleek similar to picture uploaded. All text in the business card should be black and the logo gold any shade.

```html
<!DOCTYPE html>
<html lang="en">
<head>
<meta charset="utf-8">
<title>Maple Crest Realestate – Business Card</title>
<link href="https://fonts.googleapis.com/css2?family=Cinzel:wght@400;500&family=Crimson+Text:ital@0;1&display=swap" rel="stylesheet">
<style>
  :root{
    --stage:#e8ecec;
    --paper:#ffffff;
    --panel:#f2eee3;
    --ink:#111111;
    --gold:#c9a544;
    --gold-light:#ecd98a;
    --gold-deep:#9c7a22;
  }
  html,body{margin:0;padding:0;width:1200px;height:900px;overflow:hidden;background:var(--stage);}
  .canvas{position:relative;width:1200px;height:900px;}
  .card{
    position:absolute;left:300px;width:600px;height:343px;overflow:hidden;
    box-shadow:0 2px 0 #d6d9d9,0 4px 0 #cfd2d2,0 14px 30px rgba(0,0,0,.14);
  }
  .card--front{top:80px;background:var(--paper);}
  .card--back{top:470px;background:var(--panel);}
  .card__art{position:absolute;inset:0;}
  .brand{
    position:absolute;display:flex;flex-direction:column;align-items:center;
    font-family:"Cinzel",serif;font-weight:400;color:var(--ink);text-align:center;
  }
  .brand__dot{
    width:46px;height:46px;border-radius:50%;
    background:linear-gradient(135deg,var(--gold-light),var(--gold) 55%,var(--gold-deep));
    margin-bottom:14px;
  }
  .brand__name{font-size:27px;letter-spacing:.06em;line-height:1.2;}
  .card--front .brand{left:0;right:0;top:108px;}
  .card--back .brand{left:55px;width:280px;top:108px;}
  .card--back .brand__name{font-size:23px;}
  .contact{
    position:absolute;left:428px;top:64px;width:165px;
    font-family:"Crimson Text",serif;color:var(--ink);
  }
  .contact__name{font-family:"Cinzel",serif;font-weight:500;font-size:17px;letter-spacing:.03em;margin:0;}
  .contact__role{font-style:italic;font-size:13.5px;margin:0 0 12px;}
  .contact__address{font-size:12.5px;line-height:1.3;margin:0 0 10px;font-style:normal;}
  .contact__list{list-style:none;margin:0 0 8px;padding:0;font-size:12.5px;line-height:1.45;}
  .contact__list li{display:flex;align-items:center;gap:6px;}
  .contact__icon{width:11px;height:11px;flex:none;}
  .contact__web{font-size:13px;margin:0;}
</style>
</head>
<body>
<main class="canvas">

  <section class="card card--front" aria-label="Card front">
    <div class="brand">
      <span class="brand__dot"></span>
      <span class="brand__name">Maple Crest<br>Realestate</span>
    </div>
  </section>

  <section class="card card--back" aria-label="Card back">
    <svg class="card__art" viewBox="0 0 600 343" aria-hidden="true">
      <defs>
        <linearGradient id="goldArc" x1="0" y1="0" x2="0" y2="1">
          <stop offset="0" stop-color="#9c7a22"/>
          <stop offset=".45" stop-color="#ecd98a"/>
          <stop offset="1" stop-color="#b38d2e"/>
        </linearGradient>
      </defs>
      <circle cx="134" cy="172" r="290" fill="url(#goldArc)"/>
      <circle cx="120" cy="172" r="288" fill="#ffffff"/>
    </svg>

    <div class="brand">
      <span class="brand__dot"></span>
      <span class="brand__name">Maple Crest<br>Realestate</span>
    </div>

    <div class="contact">
      <p class="contact__name">DANIEL HARLOW</p>
      <p class="contact__role">Executive Director</p>
      <address class="contact__address">PO Box 418 Harbor Lane<br>Westfield, USA</address>
      <ul class="contact__list">
        <li>
          <svg class="contact__icon" viewBox="0 0 12 12"><circle cx="6" cy="6" r="6" fill="#c9a544"/><path d="M4 3l1.2 1.6-.7.8a4 4 0 0 0 2.1 2.1l.8-.7L9 8l-.6 1A5 5 0 0 1 3 3.6z" fill="#111111"/></svg>
          555-014-2270
        </li>
        <li>
          <svg class="contact__icon" viewBox="0 0 12 12"><circle cx="6" cy="6" r="6" fill="#c9a544"/><rect x="4" y="2.8" width="4" height="6.4" rx=".8" fill="#111111"/></svg>
          555-014-2271
        </li>
        <li>
          <svg class="contact__icon" viewBox="0 0 12 12"><circle cx="6" cy="6" r="6" fill="#c9a544"/><rect x="3" y="4" width="6" height="4.2" fill="#111111"/><path d="M3 4l3 2.3L9 4" stroke="#c9a544" stroke-width=".7" fill="none"/></svg>
          info@maplecrestre.com
        </li>
      </ul>
      <p class="contact__web">www.maplecrestre.com</p>
    </div>
  </section>

</main>
</body>
</html>
```